"Tidewell Kids" needs a A5 flyer for its "Art Contest"

Tidewell Kids needs a double sided A5 Flyer that illustrates in a child-friendly look the following competition:

Search for the up and coming Sprout Sketcher. The aim of our Sprout Sketcher is to allow our children to explore the artist within them and motivate them to express their talents through the fine art of drawing and painting.

Description: I have an art school, "Tidewell Kids", where children of 3-5 years old attend and learn how to paint and draw. We are making a competition where each child gets to draw a picture which we will upload to Friendloop and parents will vote for best picture. We need to distribute to the parents a flyer with following content.

Competition Name: Sprout Sketcher

Front Side (content):
No major text on the front. Only the Logo and messages grabbing the readers attention such as "Who will be our next Artist?", "Vote for your Child", "Like Us on our Friendloop Page".

Back Side (content):
Back side content is divided into 3 sections:

Section1:
How it Works?
Every child of every class will participate. Photos will be grouped by class.
There will be a Sprout Sketcher for each class, and there will be a Sprout Sketcher for the school.

Section2:
How to Participate?
In our search for ‘Sprout Sketcher’, we will select one piece of artwork from each child in the school, photograph it and upload it to our Friendloop page.
Vote for your favourite painting by following the steps below:
1- From your friendloop account go to www.friendloop-kids.net/Tidewell Kids
and “Like Us” to become a fan
2- Click on the“Sprout Sketcher” from the application menu
3- Browse through the different classes and vote for each picture you like
4- Invite your friends to vote for the picture you like to increase the chances of winning
The artist of the painting with most “Likes” will be crowned ‘Sprout Sketcher’.

Section3:
Note (in the footer):
Please note that the winner’s photo will be displayed in our “Sprout Sketcher” Frame on our Friendloop landing page. If you do not want your child’s photograph to be posted on our Friendloop page in this manner, please let us know by sending an e-mail.
, Tidewell Kids needs a double sided A5 Flyer that illustrates in a child-friendly look the following competition:

Front Side (content):

Back Side (content):

Section1:
How it Works?

Section2:
How to Participate?

Section3:
Note (in the footer):

Parents of the children attending at our school, Parents of the children attending at our school

Painting

• Colors used in the design should be strict to our logo colors. We have 4 colors in our logo feel free to use one or all of them through out the design:
#6CB53C
#DB2718
#5D9DD5
#F4D602

The elements in our logo are playful and hand drawn and written, so the flyer design should reflect the hand made style rather than solid elements and objects., Colors used in the design should be strict to our logo colors. We have 4 colors in our logo feel free to use one or all of them through out the design:
#6CB53C
#DB2718
#5D9DD5
#F4D602

The elements in our logo are playful and hand drawn and written, so the flyer design should reflect the hand made style rather than solid elements and objects.
• Images of real children., Images of real children.

```html
<!DOCTYPE html>
<html lang="en">
<head>
<meta charset="utf-8">
<title>Sprout Sketcher — Tidewell Kids Flyer</title>
<link rel="stylesheet" href="https://fonts.googleapis.com/css2?family=Chewy&family=Fredoka:wght@600&family=Roboto:wght@700&display=swap">
<style>
  :root {
    --white: #ffffff;
    --green: #6CB53C;
    --lime: #9fcf3a;
    --red: #DB2718;
    --blue: #3d8fd6;
    --sky: #5D9DD5;
    --yellow: #F4D602;
    --sun: #f7c83a;
    --teal: #4fbf9a;
    --purple: #8a4fb8;
    --orange: #f08a1c;
    --ink: #2a2a2a;
  }
  * { margin: 0; padding: 0; box-sizing: border-box; }
  html, body { width: 845px; height: 1200px; overflow: hidden; background: var(--white); }
  .flyer { position: relative; width: 845px; height: 1200px; overflow: hidden; background: var(--white); font-family: "Roboto", Arial, sans-serif; }
  .brush { position: absolute; display: block; }
  .call-band { left: 400px; top: 0; width: 445px; height: 74px; }
  .call-text { position: absolute; right: 40px; top: 14px; color: var(--white); font-weight: 700; font-size: 36px; }
  .children-photo { position: absolute; left: 0; top: 200px; width: 845px; height: 490px;
    background: radial-gradient(ellipse at 20% 40%, #9cc9e8 0, transparent 30%),
                radial-gradient(ellipse at 50% 45%, #f08bb0 0, transparent 26%),
                radial-gradient(ellipse at 82% 42%, #f6d34a 0, transparent 26%),
                radial-gradient(ellipse at 50% 85%, #e9e4dc 0, transparent 60%),
                linear-gradient(180deg, #ffffff 0%, #f6efe8 55%, #ffffff 100%); }
  .contest-title { position: absolute; left: 0; top: 138px; width: 845px; text-align: center;
    font-family: "Fredoka", "Arial Rounded MT Bold", sans-serif; font-weight: 600; font-size: 88px; letter-spacing: 1px;
    transform: rotate(-2deg); line-height: 1; }
  .contest-title span:nth-child(7n+1) { color: var(--sky); }
  .contest-title span:nth-child(7n+2) { color: var(--red); }
  .contest-title span:nth-child(7n+3) { color: var(--green); }
  .contest-title span:nth-child(7n+4) { color: var(--orange); }
  .contest-title span:nth-child(7n+5) { color: var(--purple); }
  .contest-title span:nth-child(7n+6) { color: var(--yellow); }
  .contest-title span:nth-child(7n+7) { color: var(--red); }
  .headline-band { left: 0; top: 670px; width: 845px; height: 250px; }
  .headline { position: absolute; left: 70px; top: 712px; font-family: "Chewy", cursive; color: var(--yellow); }
  .headline-small { display: block; font-size: 48px; letter-spacing: 1px; }
  .headline-big { display: block; font-size: 84px; letter-spacing: 2px; margin-top: -4px; margin-left: 20px; }
  .vote-band { left: 390px; top: 890px; width: 455px; height: 96px; }
  .vote-text { position: absolute; left: 430px; top: 908px; color: var(--white); font-weight: 700; font-size: 44px; }
  .like-band { left: 0; top: 960px; width: 440px; height: 160px; }
  .like-text { position: absolute; left: 0; top: 1006px; width: 350px; text-align: center; color: var(--white); font-weight: 700; font-size: 31px; line-height: 1.3; }
  .join-band { left: 40px; top: 1112px; width: 370px; height: 82px; }
  .join-text { position: absolute; left: 40px; top: 1124px; width: 370px; text-align: center; font-family: "Chewy", cursive; font-size: 46px; color: var(--white); letter-spacing: 3px; }
  .school-name { position: absolute; left: 480px; top: 1060px; display: flex; align-items: center; gap: 16px; color: var(--green); font-weight: 700; font-size: 46px; }
  .school-dot { width: 54px; height: 54px; border-radius: 50%; background: var(--green); }
</style>
</head>
<body>
<main class="flyer">
  <svg class="brush call-band" viewBox="0 0 445 74" preserveAspectRatio="none" aria-hidden="true">
    <path d="M18 6 L445 0 L445 70 L30 74 L8 66 L26 58 L0 46 L22 38 L4 26 L24 18 Z" fill="var(--lime)"/>
  </svg>
  <div class="call-text">Call 55 010 20</div>

  <div class="children-photo" role="img" aria-label="Three smiling children lying on the floor drawing with coloured pencils in cups"></div>

  <h1 class="contest-title" aria-label="Sprout Sketcher"><span>S</span><span>P</span><span>R</span><span>O</span><span>U</span><span>T</span> <span>S</span><span>K</span><span>E</span><span>T</span><span>C</span><span>H</span><span>E</span><span>R</span></h1>

  <svg class="brush headline-band" viewBox="0 0 845 250" preserveAspectRatio="none" aria-hidden="true">
    <path d="M0 22 L120 10 L300 18 L480 4 L680 14 L845 6 L845 220 L700 232 L520 222 L360 240 L180 228 L0 246 Z" fill="var(--blue)"/>
  </svg>
  <h2 class="headline">
    <span class="headline-small">WHO WILL BE OUR</span>
    <span class="headline-big">NEXT ARTIST?</span>
  </h2>

  <svg class="brush like-band" viewBox="0 0 440 160" preserveAspectRatio="none" aria-hidden="true">
    <path d="M0 14 L380 0 L420 10 L400 24 L440 38 L410 60 L430 84 L402 104 L424 128 L390 150 L0 160 Z" fill="var(--sun)"/>
  </svg>
  <p class="like-text">Like Us on our<br>Friendloop Page</p>

  <svg class="brush vote-band" viewBox="0 0 455 96" preserveAspectRatio="none" aria-hidden="true">
    <path d="M30 10 L455 0 L455 92 L40 96 L14 84 L34 72 L0 58 L28 46 L6 30 L26 20 Z" fill="var(--lime)"/>
  </svg>
  <div class="vote-text">Vote for your Child</div>

  <svg class="brush join-band" viewBox="0 0 370 82" preserveAspectRatio="none" aria-hidden="true">
    <path d="M20 8 L350 0 L362 16 L346 30 L370 44 L350 60 L364 76 L30 82 L8 70 L22 56 L0 40 L20 26 L6 14 Z" fill="var(--teal)"/>
  </svg>
  <div class="join-text">JOIN NOW</div>

  <div class="school-name"><span class="school-dot" aria-hidden="true"></span>Tidewell Kids</div>
</main>
</body>
</html>
```